Software allocation system needs a business card design

We need a business card designed for our software platform - www.tolvexa.com.au

At the moment the logo and website is all black and white, we are happy for suggestions on implementing some colour throughout either the logo or business card.

Industry/Entity Type

Software

Font styles to use
Sans Serif

Colors

Designer to choose colors to be used in the design.

```html
<!DOCTYPE html>
<html lang="en">
<head>
<meta charset="utf-8">
<title>Tolvexa Business Card</title>
<link rel="stylesheet" href="https://fonts.googleapis.com/css2?family=Open+Sans:wght@300;400&family=Michroma&display=swap">
<style>
  :root {
    --backdrop: #ececec;
    --card-white: #ffffff;
    --card-black: #0c0c0c;
    --card-black-soft: #1f1f1f;
    --gold-light: #f2c25a;
    --gold: #d9a037;
    --gold-deep: #b9821f;
    --ink: #111111;
    --paper-text: #ffffff;
  }
  * { box-sizing: border-box; margin: 0; padding: 0; }
  html, body {
    width: 1200px;
    height: 900px;
    overflow: hidden;
    background: var(--backdrop);
  }
  .business-card {
    position: absolute;
    left: 150px;
    top: 170px;
    width: 900px;
    height: 560px;
    border-radius: 42px;
    overflow: hidden;
    background: var(--card-white);
    box-shadow: 0 18px 40px rgba(0,0,0,0.18);
  }
  .brand-area {
    position: absolute;
    left: 0; top: 0;
    width: 100%;
    height: 260px;
    display: flex;
    align-items: center;
    justify-content: center;
    gap: 22px;
    padding-top: 20px;
  }
  .brand-dot {
    width: 22px;
    height: 22px;
    border-radius: 50%;
    background: var(--ink);
  }
  .brand-name {
    font-family: "Open Sans", sans-serif;
    font-weight: 300;
    font-size: 96px;
    letter-spacing: 10px;
    color: var(--ink);
    text-transform: uppercase;
    line-height: 1;
  }
  .tagline-band {
    position: absolute;
    left: 0; top: 260px;
    width: 100%;
    height: 34px;
    background: linear-gradient(90deg, var(--gold-deep), var(--gold-light) 50%, var(--gold));
    display: flex;
    align-items: center;
    justify-content: center;
  }
  .tagline {
    font-family: "Michroma", sans-serif;
    font-size: 16px;
    letter-spacing: 5px;
    color: var(--ink);
    text-transform: uppercase;
  }
  .contact-area {
    position: absolute;
    left: 0; top: 294px;
    width: 100%;
    height: 266px;
    background: radial-gradient(ellipse at 70% 40%, var(--card-black-soft), var(--card-black) 75%);
    padding: 32px 0 0 62px;
  }
  .contact-list { list-style: none; }
  .contact-item {
    display: flex;
    align-items: flex-start;
    gap: 10px;
    font-family: "Open Sans", sans-serif;
    font-weight: 400;
    font-size: 28px;
    line-height: 37px;
    color: var(--paper-text);
  }
  .contact-icon {
    width: 28px;
    height: 28px;
    margin-top: 5px;
    flex: none;
    fill: var(--gold);
    stroke: var(--gold);
  }
</style>
</head>
<body>
  <div class="business-card">
    <div class="brand-area">
      <span class="brand-dot"></span>
      <span class="brand-name">Tolvexa</span>
    </div>

    <div class="tagline-band">
      <p class="tagline">Planning &amp; Compliance for Heavy Industry</p>
    </div>

    <div class="contact-area">
      <ul class="contact-list">
        <li class="contact-item">
          <svg class="contact-icon" viewBox="0 0 24 24" aria-hidden="true"><path stroke="none" d="M6.6 2.5l3 3.2-1.8 2.4c1.2 2.6 3.3 4.7 5.9 5.9l2.4-1.8 3.2 3-1.6 3.2C11 18 6 13 4.1 5.3z"/></svg>
          <span>6400 318 927</span>
        </li>
        <li class="contact-item">
          <svg class="contact-icon" viewBox="0 0 24 24" aria-hidden="true"><path stroke="none" d="M12 3L1.5 12h3v9h6v-6h3v6h6v-9h3z"/></svg>
          <span>PO Box 218<br>Harlow Bay NSW 2190</span>
        </li>
        <li class="contact-item">
          <svg class="contact-icon" viewBox="0 0 24 24" aria-hidden="true" fill="none" stroke-width="1.8"><circle cx="12" cy="12" r="9" fill="none"/><ellipse cx="12" cy="12" rx="4" ry="9" fill="none"/><path d="M3 12h18M5 7h14M5 17h14" fill="none"/></svg>
          <span>www.tolvexa.com.au</span>
        </li>
        <li class="contact-item">
          <svg class="contact-icon" viewBox="0 0 24 24" aria-hidden="true"><path stroke="none" d="M2 6h20v13H2z"/><path fill="none" stroke="#0c0c0c" stroke-width="1.6" d="M2.5 6.5L12 13l9.5-6.5M2.5 18.5l7-6M21.5 18.5l-7-6"/></svg>
          <span>hello@tolvexa.com.au</span>
        </li>
      </ul>
    </div>
  </div>
</body>
</html>
```